Please wait to be seated sign A1

We need a sign for our guests on arrival before they get seated:
A1 Size with a 2.2mm bleed
(text)
please wait - someone from our flock will be with you soon.
(must have)
Pink, Simple, Bright and Fun
We are The Velvet Heron and we put on shows so we need it to be creative. Show venue so the use of curtains or stage shows and lots of pink needs to be used. Logo centre up the the top.
Sign 2: Toilet Sign
We want something cute for a toilet directional sign
Female Flamingo and Male Flamingo
(text)
Toilets this way - if there is a cute saying or something cheeky we can do this also
Sign 3:
Platinum Members Only
Sign 4:
Gold Members Only
Sign 5:
Powder Room
Sign 6:
Arrow Sign - See photo for reference
50cm x 18cm with a 2.2mm bleed
Box Office
Sign 7:
Riverside Entry
velvetheronshows.example is the website for reference to who we are fonts and posters we use for our shows. Keep to all pink and cute.
Target Market(s)
20 - 55
Industry/Entity Type
Entertainment
Look and feel
Each slider illustrates characteristics of the customer's brand and the style your logo design should communicate.

```html
<!DOCTYPE html>
<html lang="en">
<head>
<meta charset="utf-8">
<title>Box Office – Directional Arrow Sign</title>
<link href="https://fonts.googleapis.com/css2?family=Barlow+Condensed:wght@600&display=swap" rel="stylesheet">
<style>
  :root {
    --canvas-bg: #ececef;
    --sign-bg: #f9ecf3;
    --sign-ink: #d94f98;
    --brush-deep: #e0506f;
    --brush-mid: #ec8aa3;
    --brush-soft: #f9ecf3;
  }
  html, body {
    margin: 0;
    padding: 0;
    width: 1200px;
    height: 900px;
    overflow: hidden;
    background: var(--canvas-bg);
  }
  .canvas {
    position: relative;
    width: 1200px;
    height: 900px;
  }
  .arrow-sign {
    position: absolute;
    left: 100px;
    top: 268px;
    width: 1000px;
    height: 364px;
  }
  .arrow-sign svg {
    display: block;
    width: 100%;
    height: 100%;
  }
  .sign-label {
    position: absolute;
    left: 200px;
    top: 112px;
    margin: 0;
    font-family: "Barlow Condensed", "Arial Narrow", sans-serif;
    font-weight: 600;
    font-size: 124px;
    line-height: 1;
    letter-spacing: -1px;
    color: var(--sign-ink);
    white-space: nowrap;
  }
</style>
</head>
<body>
  <main class="canvas">
    <div class="arrow-sign">
      <svg viewBox="0 0 1000 364" xmlns="http://www.w3.org/2000/svg">
        <defs>
          <clipPath id="arrow-outline">
            <polygon points="0,0 830,0 1000,192 830,364 0,364"/>
          </clipPath>
          <linearGradient id="brush-tone" x1="0" y1="0" x2="1" y2="0">
            <stop offset="0" stop-color="var(--brush-deep)"/>
            <stop offset="0.35" stop-color="var(--brush-mid)" stop-opacity="0.85"/>
            <stop offset="1" stop-color="var(--brush-soft)" stop-opacity="0"/>
          </linearGradient>
        </defs>
        <g clip-path="url(#arrow-outline)">
          <rect class="sign-face" x="0" y="0" width="1000" height="364" fill="var(--sign-bg)"/>
          <rect class="brush-feathers" role="img" aria-label="Pink painted feather brushstrokes along the left edge"
                x="0" y="0" width="190" height="364" fill="url(#brush-tone)"/>
        </g>
      </svg>
      <p class="sign-label">Box Office</p>
    </div>
  </main>
</body>
</html>
```